The Harbourlight CV consultant

The service is premium. It is aimed at people 18-30, so students and those looking to change their first job, principally in the UK but also global. It is offering a very personalised CV writing service and is much more expensive than others on offer. I am very keen that it should look simple and premium. It needs to look very professional, reflecting the aspirational jobs that the clients will be applying for.
If there were three words that summed it up: modern, clean, premium.
I am waiting for all the testimonials to come in but they need to form a major part of the website.
I am also waiting for the full logo design files so that I can upload them. In the meantime there is a copy of the logo.
Thoughts to help those yet to send a design...
This is a premium service and some of the designs have looked very generic. The focus needs to be on quality and the process mentioned in the brief. The partnership and the advantages it brings are crucial but few have mentioned that.

```html
<!DOCTYPE html>
<html lang="en">
<head>
<meta charset="utf-8">
<title>The Harbourlight CV Consultant</title>
<link href="https://fonts.googleapis.com/css2?family=Tinos:wght@400;700&family=Roboto:wght@400;500;700&display=swap" rel="stylesheet">
<style>
:root{
  --blue:#1670bf;
  --blue-dark:#0f5ea6;
  --grey-box:#6b6b6b;
  --ink:#4a4a4a;
  --muted:#8a8a8a;
  --pale:#f2f4f8;
  --footer:#262626;
  --white:#fff;
  --serif:'Tinos',serif;
  --sans:'Roboto',sans-serif;
}
*{box-sizing:border-box;margin:0;padding:0}
html,body{width:1200px;height:4202px;overflow:hidden}
body{position:relative;font-family:var(--sans);color:var(--ink);background:var(--white)}
.abs{position:absolute}
.center{left:0;width:1200px;text-align:center}

/* hero */
.hero{top:0;left:0;width:1200px;height:670px;background:linear-gradient(100deg,#3c3c3c 0%,#6c6c6a 35%,#b9b5a8 60%,#cfa94a 78%,#5a5a5a 100%)}
.hero-shade{top:0;left:0;width:1200px;height:670px;background:linear-gradient(90deg,rgba(0,0,0,.5),rgba(0,0,0,0) 60%)}
.nav{top:0;left:111px;width:978px;height:73px;background:var(--white);display:flex;align-items:center;padding:0 10px}
.logo{display:flex;align-items:center;gap:10px;font-family:var(--serif);color:var(--blue);font-size:17px;line-height:1.05}
.logo-mark{width:14px;height:14px;background:var(--blue);flex:none}
.menu{position:absolute;left:461px;top:0;height:73px;display:flex;align-items:center;gap:27px;font-size:15px;color:#666}
.menu .active{color:var(--blue);font-weight:500}
.btn{display:inline-flex;align-items:center;justify-content:center;background:var(--blue);color:var(--white);font-size:14px;border-radius:2px}
.nav .btn{position:absolute;left:836px;top:20px;width:130px;height:35px}
.hero-title{top:268px;left:111px;font-family:var(--serif);font-weight:400;font-size:46px;line-height:58px;color:var(--white);white-space:nowrap}
.hero-sub{top:398px;left:111px;font-size:16px;color:var(--white)}
.hero-cta{top:444px;left:112px;width:129px;height:34px}
.dots{top:516px;left:112px;display:flex;gap:10px}
.dot{width:16px;height:16px;border-radius:50%;background:var(--white)}
.dot.on{background:var(--blue);border:3px solid var(--white)}
.scroll-line{top:285px;left:60px;width:1px;height:225px;background:rgba(255,255,255,.7)}
.scroll-text{top:578px;left:16px;width:90px;transform:rotate(90deg);font-size:12px;letter-spacing:2px;color:var(--white);white-space:nowrap}

/* welcome */
.welcome{top:670px;left:0;width:1200px;height:716px;background:linear-gradient(180deg,#f5f6fa,#eef0f5)}
.h2{font-family:var(--serif);font-weight:400;font-size:44px;line-height:60px;text-transform:uppercase}
.h2 .grey{color:#555}
.h2 .blue{color:var(--blue)}
.rule{height:2px;width:66px;background:#777;left:567px}
.caps{font-family:var(--serif);font-size:14.5px;line-height:32px;text-transform:uppercase;color:#555}
.body-muted{font-size:14px;line-height:24px;color:var(--muted)}
.btn-outline{display:inline-flex;align-items:center;justify-content:center;border:2px solid #777;color:#555;font-size:14px;border-radius:2px;background:var(--white)}
.stat{top:1167px;width:219px;height:126px;display:flex;align-items:center;padding-left:14px;gap:10px;color:var(--white)}
.stat.blue{background:var(--blue)}
.stat.grey{background:var(--grey-box)}
.stat .num{font-size:52px;line-height:52px}
.stat .lbl{font-size:15px}

/* process */
.process{top:1386px;left:0;width:1200px;height:848px;background:linear-gradient(135deg,#1a78c9,#0f62ad)}
.step{width:300px;text-align:center;color:var(--white);font-size:16px}
.step .ring{width:118px;height:118px;margin:0 auto 20px;border:2px solid var(--white);border-radius:50%;display:flex;align-items:center;justify-content:center}

/* testimonials */
.quote-mark{top:2420px;left:164px;font-family:var(--serif);font-size:110px;color:#dcdcdc;line-height:1}
.avatar{top:2614px;left:411px;width:124px;height:124px;border-radius:50%;background:radial-gradient(circle at 50% 40%,#8a6a52,#3c7a2e 70%)}
.t-line{top:2615px;left:555px;width:1px;height:100px;background:#999}
.t-name{top:2640px;left:569px;font-family:var(--serif);font-size:26px;color:var(--blue)}
.t-role{top:2681px;left:569px;font-size:14px;color:#555}
.tdots{top:2767px;left:566px;display:flex;gap:10px}
.tdots span{width:16px;height:16px;border-radius:50%;background:#c8c8c8}
.tdots .on{background:var(--blue);border:3px solid #c8c8c8}

/* contact */
.contact{top:2886px;left:0;width:1200px;height:592px;background:linear-gradient(180deg,#d6e5f5,#eaf2fb 60%,#f4f8fd)}
.field{width:478px;height:43px;background:var(--white);border:1px solid #e1e6ee;font-size:13px;color:#555;display:flex;align-items:center;padding-left:29px}
.send{top:3282px;left:362px;width:477px;height:40px;font-weight:700;gap:22px}

/* footer */
.footer{top:3478px;left:0;width:1200px;height:724px;background:var(--footer)}
.f-sub{top:3666px;font-size:15px;line-height:22px;color:#8a8a8a}
.f-email{top:3720px;left:329px;width:407px;height:36px;border:1px solid #555;color:#aaa;font-size:13px;display:flex;align-items:center;padding-left:18px}
.f-btn{top:3720px;left:745px;width:125px;height:36px;font-weight:700;font-size:14px}
.f-logo{top:3890px;left:111px;width:278px;height:98px;background:var(--white);display:flex;align-items:center;justify-content:center}
.f-col{top:3890px;border-left:2px solid #3b3b3b;padding-left:20px;height:180px}
.f-col h3{font-family:var(--serif);font-weight:400;font-size:22px;line-height:32px;color:var(--blue);text-transform:uppercase;margin-bottom:8px;white-space:nowrap}
.f-col li{font-size:14px;line-height:28px;color:#ddd;list-style:none}
.f-item{display:flex;gap:14px;margin-bottom:10px;font-size:14px;line-height:21px;color:#ddd}
.f-item svg{flex:none;margin-top:3px}
.social{display:flex;gap:14px;margin-top:6px}
.social span{width:14px;height:14px;border-radius:50%;border:2px solid #8a8a8a}
.f-rule{top:4127px;left:111px;width:978px;height:1px;background:#444}
.copy{top:4148px;font-size:14px;color:#8a8a8a}
</style>
</head>
<body>

<!-- hero -->
<div class="abs hero" role="img" aria-label="Photo of a young woman in a yellow jumper writing notes at a desk beside a laptop showing a job search"></div>
<div class="abs hero-shade"></div>
<header class="abs nav">
  <div class="logo"><span class="logo-mark"></span><span>The Harbourlight CV Consultant</span></div>
  <nav class="menu"><span class="active">Home</span><span>Our Sevices</span><span>About Us</span><span>Contact Us</span></nav>
  <span class="btn">Apply Now</span>
</header>
<div class="abs scroll-line"></div>
<div class="abs scroll-text">SCROLL DOWN</div>
<h1 class="abs hero-title">STRUGGLING<br>WITH YOUR RESUME?</h1>
<p class="abs hero-sub">Lorem ipsum is placeholder text commonly used in the graphic, print</p>
<span class="abs btn hero-cta">Apply Now</span>
<div class="abs dots"><span class="dot"></span><span class="dot on"></span><span class="dot"></span></div>

<!-- welcome -->
<section class="abs welcome"></section>
<h2 class="abs center h2" style="top:748px"><span class="grey">Welcome to</span><br><span class="blue">Harbourlight CV Consultant</span></h2>
<div class="abs rule" style="top:878px"></div>
<p class="abs center caps" style="top:897px">Lorem ipsum dolor sit amet, consectetur adipiscing elit, sed do eiusmod tempor incididunt ut<br>labore et dolore magna aliqua. Ut enim ad minim veniam,</p>
<p class="abs center body-muted" style="top:972px">Lorem ipsum dolor sit amet, consectetur adipiscing elit, sed do eiusmod tempor incididunt ut labore et dolore<br>magna aliqua. Ut enim ad minim veniam, quis nostrud exercitation ullamco laboris nisi ut aliquip ex ea commodo<br>consequat. Duis aute irure dolor in reprehenderit in voluptate velit esse cillum dolore eu fugiat nulla pariatur. Excep-<br>teur sint occaecat cupidatat non proident, sunt in culpa qui officia deserunt mollit anim id est laborum.</p>
<span class="abs btn" style="top:1094px;left:427px;width:160px;height:35px">Learn More About Us</span>
<span class="abs btn-outline" style="top:1094px;left:643px;width:130px;height:35px">Apply Now</span>

<div class="abs stat blue" style="left:109px">
  <svg width="44" height="56" viewBox="0 0 44 56" fill="none" stroke="#fff" stroke-width="2.5"><rect x="3" y="8" width="38" height="45" rx="2"/><rect x="14" y="3" width="16" height="9" rx="2"/><path d="M11 24h22M11 32h22M11 40h22"/></svg>
  <div><div class="num">10M</div><div class="lbl">Resumes Prepared</div></div>
</div>
<div class="abs stat grey" style="left:362px">
  <svg width="52" height="52" viewBox="0 0 52 52" fill="none" stroke="#fff" stroke-width="2.5"><circle cx="24" cy="28" r="20"/><path d="M4 28h40M24 8c-7 8-7 32 0 40M24 8c7 8 7 32 0 40"/><circle cx="40" cy="12" r="7" fill="#6b6b6b"/></svg>
  <div><div class="num">10+</div><div class="lbl">Countries Served</div></div>
</div>
<div class="abs stat blue" style="left:616px">
  <svg width="54" height="54" viewBox="0 0 54 54" fill="none" stroke="#fff" stroke-width="2.5"><circle cx="22" cy="22" r="12"/><circle cx="22" cy="22" r="5"/><path d="M22 4v6M22 34v6M4 22h6M34 22h6M30 30l18 18M40 40l-4 4"/></svg>
  <div><div class="num">65+</div><div class="lbl">Industries</div></div>
</div>
<div class="abs stat grey" style="left:870px">
  <svg width="54" height="54" viewBox="0 0 54 54" fill="none" stroke="#fff" stroke-width="2.5"><circle cx="27" cy="32" r="16"/><circle cx="27" cy="28" r="5"/><path d="M18 43c2-6 16-6 18 0M8 12l2 4M27 6v5M46 12l-2 4"/></svg>
  <div><div class="num">5+</div><div class="lbl">Years in Business</div></div>
</div>

<!-- process -->
<section class="abs process"></section>
<h2 class="abs center h2" style="top:1490px;color:#fff">How it works?</h2>
<p class="abs center caps" style="top:1580px;color:#fff">Lorem ipsum dolor sit amet, consectetur adipiscing elit, sed do eiusmod tempor incididunt ut<br>labore et dolore magna aliqua. Ut enim ad minim veniam,</p>

<svg class="abs" style="top:1386px;left:0" width="1200" height="848" viewBox="0 0 1200 848" fill="none" stroke="#fff" stroke-width="1.5">
  <path d="M696 354h162"/><path d="M858 349l8 5-8 5" fill="#fff"/>
  <path d="M242 474v88"/><path d="M237 562l5 8 5-8" fill="#fff"/>
  <path d="M602 556v-88"/><path d="M597 468l5-8 5 8" fill="#fff"/>
  <path d="M953 474v88"/><path d="M948 562l5 8 5-8" fill="#fff"/>
  <path d="M337 636h170"/><path d="M507 631l8 5-8 5" fill="#fff"/>
</svg>

<div class="abs step" style="top:1681px;left:97px"><div class="ring"><svg width="64" height="64" viewBox="0 0 64 64" fill="none" stroke="#fff" stroke-width="2.5"><rect x="6" y="8" width="46" height="46" rx="2"/><path d="M6 18h46M12 13h2M18 13h2"/><path d="M22 46l4-12 22-22 8 8-22 22z"/></svg></div>CHOOSE YOUR DESIGN</div>
<div class="abs step" style="top:1681px;left:450px"><div class="ring"><svg width="64" height="64" viewBox="0 0 64 64" fill="none" stroke="#fff" stroke-width="2.5"><circle cx="32" cy="32" r="8"/><path d="M20 56c0-10 24-10 24 0"/><circle cx="16" cy="28" r="5"/><circle cx="48" cy="28" r="5"/><path d="M20 10l2 4M32 6v5M44 10l-2 4"/></svg></div>CONNECT WITH OUR EXPERT</div>
<div class="abs step" style="top:1681px;left:803px"><div class="ring"><svg width="64" height="64" viewBox="0 0 64 64" fill="none" stroke="#fff" stroke-width="2.5"><rect x="10" y="6" width="40" height="50" rx="2"/><rect x="30" y="12" width="6" height="6"/><rect x="40" y="12" width="6" height="6"/><path d="M16 26h28M16 34h28M16 42h20M40 44l14 10"/></svg></div>GET THE DRAFT COPY</div>
<div class="abs step" style="top:1963px;left:97px"><div class="ring"><svg width="64" height="64" viewBox="0 0 64 64" fill="none" stroke="#fff" stroke-width="2.5"><rect x="8" y="16" width="48" height="34" rx="2"/><path d="M8 18l24 18 24-18M8 50l18-16M56 50L38 34"/></svg></div>SHARE YOUR CONTACT DETAILS</div>
<div class="abs step" style="top:1963px;left:450px"><div class="ring"><svg width="64" height="64" viewBox="0 0 64 64" fill="none" stroke="#fff" stroke-width="2.5"><circle cx="20" cy="18" r="10"/><path d="M20 12v12M16 15h6M8 40l12-8 10 4 8-2 18 12-10 8-14-8-12 4z"/></svg></div>PAYMENT CONFIRMATION</div>
<div class="abs step" style="top:1963px;left:803px"><div class="ring"><svg width="64" height="64" viewBox="0 0 64 64" fill="none" stroke="#fff" stroke-width="3"><path d="M32 10v30M20 30l12 12 12-12M12 40v12h40V40"/></svg></div>DOWNLOAD YOUR CV</div>

<!-- testimonials -->
<h2 class="abs center h2" style="top:2311px"><span class="grey">Our happy</span><br><span class="blue">Customers says</span></h2>
<div class="abs rule" style="top:2442px"></div>
<div class="abs quote-mark">&ldquo;</div>
<p class="abs center caps" style="top:2460px">Lorem ipsum dolor sit amet, consectetur adipiscing elit, sed do eiusmod tempor incididunt ut<br>labore et dolore magna aliqua. Ut enim ad minim veniam, quis nostrud exercitation ullamco<br>laboris nisi ut aliquip ex ea commodo consequat. Duis aute irure dolor in reprehenderit in<br>voluptate velit esse</p>
<div class="abs avatar" role="img" aria-label="Portrait photo of the reviewing customer"></div>
<div class="abs t-line"></div>
<div class="abs t-name">AMELIA R. THORNTON</div>
<div class="abs t-role">DYEING MACHINE OPERATOR</div>
<div class="abs tdots"><span></span><span class="on"></span><span></span></div>

<!-- contact -->
<section class="abs contact"></section>
<h2 class="abs center h2" style="top:2976px"><span class="grey">Interested in</span><br><span class="blue">Speaking with our team?</span></h2>
<div class="abs rule" style="top:3108px"></div>
<div class="abs field" style="top:3148px;left:111px">Name</div>
<div class="abs field" style="top:3148px;left:611px">Email</div>
<div class="abs field" style="top:3215px;left:111px">Phone Number</div>
<div class="abs field" style="top:3215px;left:611px;justify-content:space-between;padding-right:26px">Mesage<svg width="10" height="6" viewBox="0 0 10 6"><path d="M0 0h10L5 6z" fill="#444"/></svg></div>
<span class="abs btn send">SEND<svg width="28" height="12" viewBox="0 0 28 12" fill="none" stroke="#fff" stroke-width="1.8"><path d="M0 6h26M21 1l5 5-5 5"/></svg></span>

<!-- footer -->
<footer class="abs footer"></footer>
<h2 class="abs center h2" style="top:3595px;color:var(--blue)">Subscribe to our news</h2>
<p class="abs center f-sub">Lorem ipsum is placeholder text commonly used in the graphic, print, and publishing industries for<br>previewing layouts and visual mockups.</p>
<div class="abs f-email">EMAIL</div>
<span class="abs btn f-btn">SUBSCRIBE</span>

<div class="abs f-logo"><div class="logo" style="font-size:19px"><span class="logo-mark"></span><span>The Harbourlight<br>CV Consultant</span></div></div>
<div class="abs f-col" style="left:423px;width:270px">
  <h3>Contact Us</h3>
  <div class="f-item"><svg width="12" height="16" viewBox="0 0 12 16"><path d="M6 0a6 6 0 0 1 6 6c0 4-6 10-6 10S0 10 0 6a6 6 0 0 1 6-6z" fill="#fff"/><circle cx="6" cy="6" r="2.2" fill="#262626"/></svg><span>14 Quayside Row, Harbour Point,<br>Co. Down, BT21 4QX</span></div>
  <div class="f-item"><svg width="14" height="14" viewBox="0 0 14 14"><path d="M3 0l3 3-2 2a9 9 0 0 0 5 5l2-2 3 3-2 3C6 14 0 8 0 3z" fill="#fff"/></svg><span>+44 1632 960 418</span></div>
  <div class="f-item"><svg width="14" height="12" viewBox="0 0 14 12" fill="none" stroke="#fff" stroke-width="1.6"><rect x="1" y="1" width="12" height="10"/><path d="M1 2l6 5 6-5"/></svg><span>hello@harbourlightcv.co.uk</span></div>
</div>
<div class="abs f-col" style="left:703px;width:160px">
  <h3>Company</h3>
  <ul><li>Home</li><li>Our Sevices</li><li>About Us</li><li>Contact Us</li></ul>
</div>
<div class="abs f-col" style="left:879px;width:250px">
  <h3>Join to<br>our community</h3>
  <div class="social"><span></span><span></span><span></span><span></span></div>
</div>
<div class="abs f-rule"></div>
<p class="abs center copy">Copyright &copy; 2024. Harbourlight CV consultant. All Rights Reserved.</p>

</body>
</html>
```